Weinetiketten für unsere neue Weinlinie SOMMERGLUT
Zielgruppe
Wir stellen qualitativ sehr hochwertige Weine, Sekte und Destillate her.
Unsere Zielgruppe sind kaufkräftige Kunden zwischen 25-70 Jahren.
Aufgabenstellung
Edel, schlicht und zeitlos soll das neue Etikett werden, nur leicht verspielt.
Mit hohem Wiedererkennungswert, da die Wein auch im Fachhandel (in Regalen) präsentiert werden. Der Name "Sommerglut" steht für expressive Weine voller Fruchtaromen und Düften.

```html
<!DOCTYPE html>
<html lang="de">
<head>
<meta charset="utf-8">
<title>Sommerglut – Weinetikett</title>
<link rel="stylesheet" href="https://fonts.googleapis.com/css2?family=Tenor+Sans&display=swap">
<style>
  :root {
    --backdrop: #f3f3f3;
    --label-white: #ffffff;
    --label-black: #0f0f10;
    --gold: #a8925f;
    --lime-rule: #c6cc4a;
    --ink: #141414;
  }
  html, body {
    margin: 0;
    padding: 0;
    width: 1200px;
    height: 3001px;
    overflow: hidden;
    background: var(--backdrop);
  }
  .wine-label {
    display: block;
    width: 1200px;
    height: 3001px;
    font-family: "Tenor Sans", "Optima", sans-serif;
  }
  .label-panel-dark { fill: var(--label-black); }
  .label-panel-light { fill: var(--label-white); }
  .line-name { fill: var(--gold); }
  .house-name { fill: var(--gold); }
  .divider { stroke: var(--lime-rule); stroke-width: 4; }
  .varietal, .vintage { fill: var(--ink); }
  .brand-dot { fill: var(--gold); }
  .brand-name { fill: var(--gold); }
</style>
</head>
<body>
<svg class="wine-label" viewBox="0 0 1200 3001" xmlns="http://www.w3.org/2000/svg" role="img" aria-label="Weinetikett Sommerglut Zorva, Cabernet Sauvignon 2009">
  <rect class="label-panel-dark" x="200" y="345" width="935" height="2585"/>
  <rect class="label-panel-light" x="200" y="400" width="686" height="2442"/>

  <text class="line-name" x="486" y="1984" transform="rotate(-90 486 1984)"
        font-size="300" textLength="1474" lengthAdjust="spacingAndGlyphs">SOMMERGLUT</text>

  <text class="house-name" x="273" y="2193" font-size="188"
        textLength="543" lengthAdjust="spacingAndGlyphs">ZORVA</text>

  <line class="divider" x1="251" y1="2402" x2="856" y2="2402"/>

  <text class="varietal" x="543" y="2593" font-size="62" text-anchor="middle">CABERNET</text>
  <text class="varietal" x="543" y="2666" font-size="62" text-anchor="middle">SAUVIGNON</text>
  <text class="vintage" x="543" y="2754" font-size="48" text-anchor="middle">2009</text>

  <circle class="brand-dot" cx="882" cy="1368" r="45"/>
  <text class="brand-name" x="945" y="1385" font-size="48">ZORVA</text>
</svg>
</body>
</html>
```